KTR Engineering Pty Ltd

I have already had Corvale welding and fabrication cards made , my business has changed too KTR engineering Pty Ltd so I need my logo changed on the cards
one side have my logo then the other side have what we do.
front side logo and details
owner /operator : Lachlan Meravic
email: ktr.works@ironvalemail.com
number: 0491537204
ABN: 47 261 538 902
ACN: 718 352 946
on back have in dot points what we do:
* structural steel erection
* precast panels
* site welding
*steel alteration & repair
* rigging & dogging
*labour hire
all details in breif

```html
<!DOCTYPE html>
<html lang="en">
<head>
<meta charset="UTF-8">
<title>KTR Engineering Pty Ltd – Business Cards</title>
<link href="https://fonts.googleapis.com/css2?family=Lato:wght@400;700;900&display=swap" rel="stylesheet">
<style>
  :root {
    --backdrop: #3b3b3d;
    --rust: #8b4634;
    --navy: #16243a;
    --paper: #ffffff;
    --ink: #1d1d1f;
  }
  * { box-sizing: border-box; margin: 0; padding: 0; }
  html, body {
    width: 1200px; height: 689px; overflow: hidden;
    background: var(--backdrop);
    font-family: "Lato", sans-serif;
  }
  .stage { position: relative; width: 1200px; height: 689px; }
  .card {
    position: absolute; top: 180px;
    width: 540px; height: 330px;
    border-radius: 26px; overflow: hidden;
  }

  /* Services side */
  .card--services { left: 40px; background: var(--rust); color: var(--paper); }
  .card--services .brand {
    position: absolute; left: 40px; top: 135px; width: 200px;
    display: flex; align-items: center; gap: 10px;
  }
  .brand__dot { width: 14px; height: 14px; border-radius: 50%; flex: none; }
  .card--services .brand__dot { background: var(--paper); }
  .brand__name { font-weight: 900; font-size: 19px; line-height: 1.15; letter-spacing: .3px; }
  .card--services .divider {
    position: absolute; left: 262px; top: 80px; width: 1px; height: 170px;
    background: rgba(255,255,255,.85);
  }
  .services {
    position: absolute; left: 290px; top: 92px; list-style: none;
    font-size: 16px; line-height: 25px;
  }
  .services li { display: flex; align-items: center; gap: 9px; }
  .services svg { width: 13px; height: 13px; flex: none; }

  /* Contact side */
  .card--contact { left: 620px; background: var(--paper); color: var(--navy); }
  .edge { position: absolute; left: 0; top: 0; width: 40px; height: 330px; }
  .card--contact .brand {
    position: absolute; right: 34px; top: 48px; width: 210px;
    display: flex; align-items: center; gap: 10px; color: var(--navy);
  }
  .card--contact .brand__dot { background: var(--rust); }
  .person { position: absolute; left: 60px; top: 118px; }
  .person__name { font-weight: 900; font-size: 30px; color: var(--navy); }
  .person__role { font-size: 18px; color: var(--rust); margin-top: 2px; }
  .contacts { position: absolute; left: 60px; top: 196px; list-style: none; font-size: 16px; color: var(--ink); }
  .contacts li { display: flex; align-items: center; gap: 10px; line-height: 25px; }
  .contacts svg { width: 15px; height: 15px; flex: none; }
  .rule { position: absolute; left: 60px; right: 34px; top: 256px; height: 1.5px; background: var(--navy); }
  .registry { position: absolute; left: 60px; top: 266px; font-size: 15px; line-height: 22px; color: var(--ink); }
  .registry span { color: var(--rust); }
</style>
</head>
<body>
<main class="stage">

  <section class="card card--services" aria-label="Services side">
    <div class="brand">
      <span class="brand__dot"></span>
      <span class="brand__name">KTR Engineering Pty Ltd</span>
    </div>
    <div class="divider"></div>
    <ul class="services">
      <li><svg viewBox="0 0 14 14"><circle cx="7" cy="7" r="7" fill="#fff"/><path d="M3.8 7.2l2.1 2.1 4.3-4.4" stroke="#8b4634" stroke-width="1.8" fill="none"/></svg>Structural Steel Erection</li>
      <li><svg viewBox="0 0 14 14"><circle cx="7" cy="7" r="7" fill="#fff"/><path d="M3.8 7.2l2.1 2.1 4.3-4.4" stroke="#8b4634" stroke-width="1.8" fill="none"/></svg>Precast Panels</li>
      <li><svg viewBox="0 0 14 14"><circle cx="7" cy="7" r="7" fill="#fff"/><path d="M3.8 7.2l2.1 2.1 4.3-4.4" stroke="#8b4634" stroke-width="1.8" fill="none"/></svg>Site Welding</li>
      <li><svg viewBox="0 0 14 14"><circle cx="7" cy="7" r="7" fill="#fff"/><path d="M3.8 7.2l2.1 2.1 4.3-4.4" stroke="#8b4634" stroke-width="1.8" fill="none"/></svg>Steel Alteration &amp; Repair</li>
      <li><svg viewBox="0 0 14 14"><circle cx="7" cy="7" r="7" fill="#fff"/><path d="M3.8 7.2l2.1 2.1 4.3-4.4" stroke="#8b4634" stroke-width="1.8" fill="none"/></svg>Rigging &amp; Dogging</li>
      <li><svg viewBox="0 0 14 14"><circle cx="7" cy="7" r="7" fill="#fff"/><path d="M3.8 7.2l2.1 2.1 4.3-4.4" stroke="#8b4634" stroke-width="1.8" fill="none"/></svg>Labour Hire</li>
    </ul>
  </section>

  <section class="card card--contact" aria-label="Contact side">
    <svg class="edge" viewBox="0 0 40 330" preserveAspectRatio="none">
      <polygon points="0,0 10,0 24,230 0,240" fill="var(--navy)"/>
      <polygon points="0,240 24,230 30,250 14,250 40,330 0,330" fill="var(--rust)"/>
    </svg>
    <div class="brand">
      <span class="brand__dot"></span>
      <span class="brand__name">KTR Engineering Pty Ltd</span>
    </div>
    <div class="person">
      <p class="person__name">Lachlan Meravic</p>
      <p class="person__role">Owner/Operator</p>
    </div>
    <ul class="contacts">
      <li><svg viewBox="0 0 16 16"><path d="M4 1.5l2.3 3-1.4 1.6c.9 2 2.5 3.6 4.5 4.5l1.6-1.4 3 2.3-1.4 2.2C7.6 13.3 2.7 8.4 1.8 3.4z" fill="var(--rust)"/></svg>0491537204</li>
      <li><svg viewBox="0 0 16 16"><rect x="1" y="3" width="14" height="10" fill="var(--rust)"/><path d="M1 3l7 6 7-6" stroke="#fff" stroke-width="1.2" fill="none"/></svg>ktr.works@ironvalemail.com</li>
    </ul>
    <div class="rule"></div>
    <p class="registry"><span>ABN:</span> 47 261 538 902<br><span>ACN:</span> 718 352 946</p>
  </section>

</main>
</body>
</html>
```